TIVARELCAP web-presence redisign

We would like to have our existing web-presence redesigned. Have a look at www.tivarel.ch (please use explorer). To the existing 11 pages we would add one more.

```html
<!DOCTYPE html>
<html lang="de">
<head>
<meta charset="utf-8">
<title>Tivarel Zahnarztpraxis</title>
<link href="https://fonts.googleapis.com/css2?family=Open+Sans:wght@400;600;700&family=Oswald:wght@600&family=Cinzel:wght@700&display=swap" rel="stylesheet">
<style>
:root{
  --dark:#2f3031;
  --darker:#1e1f20;
  --header:#eeeeee;
  --blue:#4db6e2;
  --blue-deep:#1f93c8;
  --content:#e8e8e8;
  --white:#f5f4f4;
  --text:#555;
  --yellow:#f0c419;
  --orange:#e8a21b;
  --field:#4b4b4b;
}
*{margin:0;padding:0;box-sizing:border-box}
html,body{width:939px;height:1200px;overflow:hidden}
body{font-family:"Open Sans",Arial,sans-serif;background:var(--white);position:relative;color:var(--text)}
.abs{position:absolute}
.topbar{left:0;top:0;width:939px;height:32px;background:var(--dark);font-size:11px;color:#fff}
.topbar span{position:absolute;top:9px}
.topbar .active{color:var(--yellow)}
.topbar .lang{color:var(--blue)}
.search{left:721px;top:0;width:197px;height:32px;background:#5a5b5c;color:#fff;font-size:10px;padding:14px 12px}
.header{left:0;top:32px;width:939px;height:74px;background:var(--header)}
.social-panel{left:721px;top:32px;width:197px;height:48px;background:#fff;border-radius:0 0 6px 6px;box-shadow:0 2px 3px rgba(0,0,0,.25)}
.social{top:41px;width:31px;height:31px;border-radius:6px}
.logo-mark{left:36px;top:36px;width:40px;height:40px;border-radius:50%;background:var(--orange)}
.logo-name{left:84px;top:38px;font-family:"Cinzel",serif;font-size:30px;color:#8a6a2b;line-height:1}
.logo-sub{left:116px;top:66px;font-family:"Cinzel",serif;font-size:19px;color:#8a6a2b}
.call{left:452px;top:42px;font-size:15px;font-weight:600;color:var(--blue)}
.phone-num{left:452px;top:61px;font-size:15px;font-weight:700;color:#333}
.phone-icon{left:416px;top:44px}
.rule{left:0;top:106px;width:939px;height:7px;background:var(--darker)}
.band{left:0;top:113px;width:939px;height:320px;background:var(--blue-deep)}
.nav{left:83px;top:94px;width:785px;height:34px;background:var(--blue);box-shadow:0 6px 8px rgba(0,0,0,.3);display:flex;font-size:12px;color:#fff}
.nav a{position:absolute;top:10px;color:#fff;text-decoration:none}
.nav .current{position:absolute;left:189px;top:0;width:123px;height:34px;background:var(--blue-deep)}
.slider{left:28px;top:149px;width:889px;height:324px;background:linear-gradient(90deg,#6c8a3e 0%,#8fb35a 45%,#c9b79c 70%,#e6d2bd 100%);box-shadow:0 8px 10px rgba(0,0,0,.3)}
.arrow{top:257px;width:26px;height:54px;background:#111;color:#f0c419;font-size:18px;text-align:center;line-height:54px}
.cap{left:28px;font-size:18px;padding:0 12px;height:38px;line-height:38px;font-weight:600}
.cap1{top:340px;background:#111;color:#fff}
.cap2{top:393px;background:#fff;color:#111}
.dropdown{left:271px;top:130px;width:188px;height:131px;background:#3a3a3a;font-size:12px;color:#fff}
.dropdown div{height:31px;line-height:31px;padding-left:11px}
.dropdown .sel{background:var(--blue-deep)}
.content{left:0;top:473px;width:939px;height:377px;background:var(--content)}
.h1{left:27px;top:530px;font-size:20px;color:#555;font-weight:400}
.thumb{left:27px;top:571px;width:174px;height:125px;background:#fff;padding:5px}
.thumb div{width:100%;height:100%;background:linear-gradient(#d97a80,#f3eaea 50%,#c9505a)}
.body1{left:214px;top:566px;width:402px;font-size:12.5px;line-height:19px;text-align:justify}
.body2{left:30px;top:710px;width:586px;font-size:12.5px;line-height:19px}
.booking{left:632px;top:522px;width:284px;height:305px;border-radius:6px;background:linear-gradient(#3a3a3a,#0d0d0d)}
.tab{left:689px;top:518px;width:167px;height:42px;background:var(--blue-deep);color:#fff;font-size:13px;text-align:center;line-height:42px;box-shadow:0 4px 4px rgba(0,0,0,.4)}
.field{left:658px;width:227px;height:28px;background:var(--field);border-radius:6px;color:#ddd;font-size:12px;padding:6px 15px}
.submit{left:704px;top:772px;width:137px;height:30px;background:linear-gradient(#f2b52a,#d98a12);border-radius:6px;color:#222;font-size:14px;text-align:center;line-height:30px}
.zhead{left:258px;top:866px;font-family:"Oswald",sans-serif;font-size:19px;color:#111;letter-spacing:1px}
.zline{top:877px;height:3px;background:#111}
.avatar{left:258px;top:916px;width:97px;height:97px;border-radius:50%;border:3px solid var(--blue);background:linear-gradient(#d6b48f,#f0d8c0)}
.quote{left:50px;top:1043px;width:545px;font-size:13.5px;line-height:22px;text-align:center;color:#444}
.quote b{color:var(--blue)}
.video{left:632px;top:878px;width:284px;height:228px;border:2px solid #111;background:#fff;box-shadow:0 6px 8px rgba(0,0,0,.3)}
.vtitle{left:632px;top:878px;width:284px;height:37px;background:#111;color:var(--blue);font-family:"Oswald",sans-serif;font-size:19px;text-align:center;line-height:37px}
.vimg{left:636px;top:915px;width:276px;height:160px;background:linear-gradient(#b9cbd9,#5d8fc4)}
.vbar{left:636px;top:1075px;width:276px;height:27px;background:linear-gradient(#eee,#aaa)}
.footer-line{left:0;top:1156px;width:939px;height:9px;background:var(--blue)}
.footer{left:0;top:1165px;width:939px;height:35px;background:var(--dark);color:#fff;font-size:10px}
.footer span{position:absolute;top:12px}
</style>
</head>
<body>
<div class="abs topbar">
  <span class="active" style="left:341px">HOME</span>
  <span style="left:429px">Language :</span>
  <span class="lang" style="left:493px">English (UK)</span>
  <span class="lang" style="left:563px">|</span>
  <span class="lang" style="left:579px">German</span>
  <span style="left:659px">Help</span>
</div>
<div class="abs header"></div>
<div class="abs search">Search . . .</div>
<div class="abs social-panel"></div>
<div class="abs social" style="left:755px;background:#2fa3dc"></div>
<div class="abs social" style="left:791px;background:#c4302b"></div>
<div class="abs social" style="left:827px;background:#3b5998"></div>
<div class="abs social" style="left:863px;background:#0e76a8"></div>

<div class="abs logo-mark"></div>
<div class="abs logo-name">TIVAREL</div>
<div class="abs logo-sub">Zahnarztpraxis</div>

<svg class="abs phone-icon" width="26" height="36" viewBox="0 0 26 36" aria-hidden="true">
  <path d="M7 2 L13 2 L13 9 L9 11 Q9 18 11 25 L15 25 L16 32 L10 34 Q2 20 7 2Z" fill="#555"/>
</svg>
<div class="abs call">Rufen Sie an für Beratung!</div>
<div class="abs phone-num">301 - 480 - 7320</div>

<div class="abs rule"></div>
<div class="abs band"></div>

<nav class="abs nav">
  <div class="current"></div>
  <a style="left:112px">HOME</a>
  <a style="left:202px">ZAHNMEDIZIN &#9662;</a>
  <a style="left:338px">DENTALHYGIENE</a>
  <a style="left:486px">TEAM</a>
  <a style="left:573px">KONTAKT</a>
</nav>

<div class="abs slider" role="img" aria-label="Lächelnde Frau mit blonden Haaren vor grünem Hintergrund"></div>
<div class="abs arrow" style="left:28px;border-radius:0 27px 27px 0">&#8250;</div>
<div class="abs arrow" style="left:891px;border-radius:27px 0 0 27px">&#8249;</div>
<div class="abs cap cap1">"In bietet persönliche Betreuung mit den</div>
<div class="abs cap cap2">neuesten Fortschritten in der Zahnmedizin verpflichtet"</div>

<div class="abs dropdown">
  <div class="sel">Zahnarztbehandlung</div>
  <div>Kompetenzen</div>
  <div>Zahnärztliche Behandlung</div>
  <div>Notfälle</div>
</div>

<section class="abs content"></section>
<h1 class="abs h1">Zahnarztbehandlung</h1>
<div class="abs thumb"><div role="img" aria-label="Nahaufnahme eines Lächelns mit weissen Zähnen"></div></div>
<p class="abs body1">Durch eine sanfte zahnmedizinische Behandlungsmethode soll dem Patienten eine angstfreie Behandlung ermöglicht werden. Davon profitieren insbesondere auch Kinder und Phobiepatienten. Aufgrund der chirurgischen Zusatzausbildung von Dr. Lena Marwick-Ost sind das Entfernen von Weisheitszähnen oder das Einsetzen von Implantaten nach modernster Methode eine Selbstverständlichkeit. Im Hinblick auf das gesundheitliche Wohlbefin -</p>
<p class="abs body2">den der Patienten werden "weisse" Füllungen (Komposit anstelle von Amalgam) und Keramik-Inlays bzw. Kronen empfohlen.</p>

<div class="abs booking"></div>
<div class="abs tab">Buchen Sie einen Termin</div>
<div class="abs field" style="top:585px">Name</div>
<div class="abs field" style="top:622px">Email</div>
<div class="abs field" style="top:659px;height:99px">Nachricht</div>
<div class="abs submit">Einreichen</div>

<div class="abs zline" style="left:28px;width:199px"></div>
<div class="abs zline" style="left:372px;width:243px"></div>
<h2 class="abs zhead">ZEUGNISSE</h2>
<div class="abs avatar" role="img" aria-label="Porträt einer zufriedenen Patientin"></div>
<p class="abs quote">" Ich möchte Ihnen aus tiefstem Herzen danken, dass sie mir meine perfekte Lächeln und jüngeren Teint, hat mein Selbstvertrauen enorm gewachsen. Jas, sind Ihre Talente endlos." - <b>Miriam</b></p>

<div class="abs video"></div>
<div class="abs vtitle">ZAHNBEHANDLUNG VIDEO</div>
<div class="abs vimg" role="img" aria-label="Videostandbild: Kind mit Lupe in der Zahnarztpraxis"></div>
<div class="abs vbar">
  <svg width="276" height="27" viewBox="0 0 276 27" aria-hidden="true">
    <rect x="6" y="8" width="28" height="11" rx="5" fill="#ccc" stroke="#888"/>
    <rect x="42" y="11" width="196" height="5" fill="#333"/>
    <rect x="42" y="11" width="98" height="5" fill="#d32020"/>
    <rect x="128" y="6" width="10" height="14" rx="2" fill="#ddd" stroke="#888"/>
    <rect x="244" y="8" width="22" height="11" rx="5" fill="#ccc" stroke="#888"/>
  </svg>
</div>
<svg class="abs" style="left:884px;top:1002px" width="20" height="70" viewBox="0 0 20 70" aria-hidden="true">
  <rect x="2" y="2" width="16" height="66" rx="8" fill="#ddd" stroke="#888"/>
  <rect x="6" y="22" width="8" height="42" rx="4" fill="#3aa0e0"/>
  <rect x="3" y="18" width="14" height="6" rx="2" fill="#eee" stroke="#777"/>
</svg>

<div class="abs footer-line"></div>
<svg class="abs" style="left:466px;top:1163px" width="20" height="10" viewBox="0 0 20 10" aria-hidden="true"><path d="M0 0H20L10 10Z" fill="#4db6e2"/></svg>
<footer class="abs footer">
  <span style="left:26px">Home &nbsp;|&nbsp; Zahnmedizin &nbsp;|&nbsp; Dentalhygiene &nbsp;|&nbsp; Team &nbsp;|&nbsp; Kontakt</span>
  <span style="left:759px">2014 Tivarel &nbsp;Zahnarztpraxis.com</span>
</footer>
</body>
</html>
```